Webdesign for Non profit Diabetes education company

We are looking for a website design for our company.

We just created the company Glucose Guidance Circle

The concept for the company is to educate diabetics with resources that will help them manage their Diabetes. The list of advisers will be dietitians, podiatrist, diabetic educators, and fitness centers.

Please see attached logo. I like the logo to include an image that connects people together.

I've attached our logo, please use the colors in the design of the site.

Creativity is encouraged. Have fun with this project. We are looking for a professional site but not to corporate.

The page must be written in HTML 5 and be responsive built for mobile. You can use bootstrap, jquery, or angular JS.

Wordpress or wix will not be accepted.

The website will be hosted at www.glucoseguidancecircle.example

Requirements
Must have
• The page must be written in HTML 5 and be responsive built for mobile. You can use bootstrap, jquery, or angular JS.
• The landing page should include a splash page. Please incorporate the logo and the
Should not have
• Wordpress or wix will not be accepted.

```html
<!DOCTYPE html>
<html lang="en">
<head>
<meta charset="utf-8">
<title>Glucose Guidance Circle – Diabetes Facts and Care Network</title>
<link rel="stylesheet" href="https://fonts.googleapis.com/css2?family=Arimo:wght@400;500;600;700&display=swap">
<style>
  :root {
    --blue: #6b93cf;
    --blue-light: #8fb0de;
    --pink: #f85f8a;
    --ink: #2b2b2b;
    --text: #383838;
    --panel: #e9e9e9;
    --white: #ffffff;
  }
  * { margin: 0; padding: 0; box-sizing: border-box; }
  html, body { width: 1200px; height: 1200px; overflow: hidden; background: var(--white); }
  body { position: relative; font-family: "Arimo", Arial, sans-serif; color: var(--text); }

  .stat { position: absolute; top: 0; width: 320px; }
  .stat__ring { position: absolute; top: 30px; left: 0; width: 192px; height: 192px; }
  .stat__value {
    position: absolute; top: 30px; left: 0; width: 192px; height: 192px;
    display: flex; align-items: center; justify-content: center;
    font-size: 19.5px; font-weight: 600; color: var(--ink); letter-spacing: 0.4px;
  }
  .stat__title { position: absolute; top: 230px; left: 0; font-size: 24px; line-height: 28px; font-weight: 700; color: var(--ink); }
  .stat__text { position: absolute; top: 257px; left: 0; width: 300px; font-size: 16.7px; line-height: 20px; }

  .stat--total { left: 54px; }
  .stat--diagnosed { left: 458px; }
  .stat--undiagnosed { left: 837px; }
  .stat--total .stat__title, .stat--total .stat__text,
  .stat--diagnosed .stat__title, .stat--diagnosed .stat__text,
  .stat--undiagnosed .stat__title, .stat--undiagnosed .stat__text { left: 0; }

  .providers {
    position: absolute; left: 24px; top: 376px; width: 1138px; height: 810px;
    background: var(--panel);
  }
  .providers__heading {
    position: absolute; left: 30px; top: 54px; width: 1024px;
    font-size: 21px; font-weight: 500; color: #111; letter-spacing: 0.2px;
    padding-bottom: 1px; border-bottom: 1.5px solid #222;
  }
  .provider { position: absolute; width: 290px; }
  .provider__icon {
    width: 124px; height: 124px; border-radius: 50%; background: var(--white);
    display: flex; align-items: center; justify-content: center;
  }
  .provider__icon span {
    display: block; width: 72px; height: 64px; border-radius: 14px;
    background: linear-gradient(160deg, var(--blue) 0%, var(--blue-light) 70%, var(--pink) 100%);
  }
  .provider__icon--warm span { background: linear-gradient(160deg, var(--blue) 0%, var(--blue-light) 45%, var(--pink) 100%); }
  .provider__title { margin-top: 22px; font-size: 23px; line-height: 26px; font-weight: 600; color: var(--ink); }
  .provider__text { margin-top: 12px; width: 282px; font-size: 17px; line-height: 20px; }

  .provider--pedorthist { left: 30px; top: 104px; }
  .provider--educator { left: 437px; top: 104px; }
  .provider--endocrinologist { left: 844px; top: 104px; }
  .provider--nutritionist { left: 30px; top: 452px; }
  .provider--podiatrist { left: 437px; top: 452px; }
</style>
</head>
<body>

<section class="stat stat--total">
  <svg class="stat__ring" viewBox="0 0 192 192" aria-hidden="true">
    <circle cx="96" cy="96" r="88" fill="none" stroke="var(--blue)" stroke-width="15"/>
  </svg>
  <div class="stat__value">30.3 MILLION</div>
  <h2 class="stat__title">Total</h2>
  <p class="stat__text">An estimated 30.3 million people have diabetes (9.4 percent of the U.S. population)</p>
</section>

<section class="stat stat--diagnosed">
  <svg class="stat__ring" viewBox="0 0 192 192" aria-hidden="true">
    <circle cx="96" cy="96" r="88" fill="none" stroke="var(--blue)" stroke-width="15"/>
    <circle cx="96" cy="96" r="88" fill="none" stroke="var(--pink)" stroke-width="15"
      stroke-dasharray="72 481" stroke-dashoffset="-8" transform="rotate(-90 96 96)"/>
  </svg>
  <div class="stat__value">23.1 MILLION</div>
  <h2 class="stat__title">Diagnosed</h2>
  <p class="stat__text">An estimated 23.1 million people have been diagnosed with diabetes (7.2 percent of the U.S. population)</p>
</section>

<section class="stat stat--undiagnosed">
  <svg class="stat__ring" viewBox="0 0 192 192" aria-hidden="true">
    <circle cx="96" cy="96" r="88" fill="none" stroke="var(--pink)" stroke-width="15"/>
    <circle cx="96" cy="96" r="88" fill="none" stroke="var(--blue)" stroke-width="15"
      stroke-dasharray="72 481" stroke-dashoffset="-6" transform="rotate(-90 96 96)"/>
  </svg>
  <div class="stat__value">7.2 MILLION</div>
  <h2 class="stat__title">Undiagnosed</h2>
  <p class="stat__text">An estimated 7.2 million adults, ages 18 years or older are undiagnosed (23.8 percent of people with diabetes)</p>
</section>

<section class="providers">
  <h2 class="providers__heading">OUR NETWORK OF HEALTHCARE PROVIDERS WILL HELP YOU MANAGE YOUR DIABETES.</h2>

  <article class="provider provider--pedorthist">
    <div class="provider__icon" role="img" aria-label="Icon: foot resting on a supportive shoe insert"><span></span></div>
    <h3 class="provider__title">Pedorthist</h3>
    <p class="provider__text">A professional who has specialized training in foot evaluation and modification of footwear and supportive devices such as inserts, to address conditions which affect the feet and lower limbs caused by disease, defect or injury.</p>
  </article>

  <article class="provider provider--educator">
    <div class="provider__icon provider__icon--warm" role="img" aria-label="Icon: health professional beside a glucose meter"><span></span></div>
    <h3 class="provider__title">Diabetic Educator</h3>
    <p class="provider__text">A health professional who possesses knowledge of and experience in diabetes prevention, pre-diabetes, and diabetes management. Their main goal is to achieve individualized behavioral and treatment goals that reduce risks and optimize healthy lifestyles.</p>
  </article>

  <article class="provider provider--endocrinologist">
    <div class="provider__icon provider__icon--warm" role="img" aria-label="Icon: blood glucose meter and finger test"><span></span></div>
    <h3 class="provider__title">Endocrinologist</h3>
    <p class="provider__text">A physician who specializes in treating disorders of the endocrine system, such as diabetes.</p>
  </article>

  <article class="provider provider--nutritionist">
    <div class="provider__icon" role="img" aria-label="Icon: apple on a kitchen scale"><span></span></div>
    <h3 class="provider__title">Nutritionists</h3>
    <p class="provider__text">An expert in dietetics; which includes human nutrition and the regulation of diet. A dietitian alters their patient's nutrition based upon their medical condition and individual needs.</p>
  </article>

  <article class="provider provider--podiatrist">
    <div class="provider__icon provider__icon--warm" role="img" aria-label="Icon: hands examining a foot"><span></span></div>
    <h3 class="provider__title">Podiatrist</h3>
    <p class="provider__text">A doctor qualified and trained to diagnose and treat conditions affecting the foot, ankle, and related structures of the leg.</p>
  </article>
</section>

</body>
</html>
```